Quiet River Psalter Reflections for Every Season of Long Waiting

This is not an Eastern meditation method. No images or themes from guru style or Eastern meditations from Hinduism or Buddhism will work. This is a Biblical Christian-based method. Some sort of Divine Light from Heaven may be the look. Some "ancient scroll" for the title to be written in may work.

```html
<!DOCTYPE html>
<html lang="en">
<head>
<meta charset="utf-8">
<title>Quiet River Psalter — Book Cover</title>
<link href="https://fonts.googleapis.com/css2?family=Cormorant+Garamond:wght@500&family=EB+Garamond:wght@400&family=Kalam:wght@400&display=swap" rel="stylesheet">
<style>
  :root {
    --page-bg: #ffffff;
    --night-top: #2a2a44;
    --night-mid: #252238;
    --night-deep: #1e1a2e;
    --ink-light: #f6f3ee;
    --ink-soft: #e4e0da;
    --gold: #e9c77c;
    --sky-teal: #3e8a94;
    --sky-orange: #f0a46a;
    --sun-glow: #fbe9c8;
    --wave-blue: #1f6e7c;
  }
  * { margin: 0; padding: 0; box-sizing: border-box; }
  html, body {
    width: 1200px;
    height: 1200px;
    overflow: hidden;
    background: var(--page-bg);
  }
  .canvas {
    position: relative;
    width: 1200px;
    height: 1200px;
  }
  .cover {
    position: absolute;
    left: 243px;
    top: 50px;
    width: 714px;
    height: 1100px;
    overflow: hidden;
    background: linear-gradient(180deg, var(--night-top) 0%, var(--night-mid) 55%, var(--night-deep) 100%);
  }
  .cover-art {
    position: absolute;
    left: 0;
    top: 0;
    width: 100%;
    height: 470px;
    background:
      radial-gradient(ellipse 180px 110px at 55% 78%, var(--sun-glow) 0%, rgba(251,233,200,0.55) 45%, rgba(251,233,200,0) 100%),
      radial-gradient(ellipse 260px 220px at 30% 35%, var(--wave-blue) 0%, rgba(31,110,124,0.6) 55%, rgba(31,110,124,0) 100%),
      linear-gradient(180deg, var(--sky-teal) 0%, #6a9c9c 30%, var(--sky-orange) 62%, #c9866a 80%, var(--night-top) 100%);
  }
  .cover-text {
    position: absolute;
    left: 0;
    width: 100%;
    text-align: center;
    color: var(--ink-light);
  }
  .title {
    top: 452px;
    font-family: "Cormorant Garamond", "EB Garamond", serif;
    font-weight: 500;
    font-size: 96px;
    line-height: 108px;
    letter-spacing: -1px;
  }
  .subtitle {
    top: 672px;
    font-family: "EB Garamond", serif;
    font-size: 33px;
    letter-spacing: 3px;
    text-transform: uppercase;
    color: var(--ink-soft);
  }
  .tagline {
    top: 822px;
    font-family: "Kalam", cursive;
    font-size: 32px;
    color: var(--gold);
    letter-spacing: 1px;
  }
  .author {
    top: 980px;
    font-family: "Cormorant Garamond", "EB Garamond", serif;
    font-weight: 500;
    font-size: 64px;
    letter-spacing: -0.5px;
  }
</style>
</head>
<body>
<div class="canvas">
  <div class="cover">
    <div class="cover-art" role="img" aria-label="Photograph of a curling turquoise ocean wave against a glowing sunset sky over dark water"></div>
    <h1 class="cover-text title">Quiet River<br>Psalter</h1>
    <p class="cover-text subtitle">Reflections</p>
    <p class="cover-text tagline">For Every Season of Long Waiting</p>
    <p class="cover-text author">Thomas Whitley</p>
  </div>
</div>
</body>
</html>
```